Website Design for Morvane.com

We are starting up a business to sell Blutooth devices. Initially speakers and headphones

Morvane of Norway
Leading technology, uncompromised quality.

Specialist in top quality bluetooth equipment
We specialize in design and production of top

```html
<!DOCTYPE html>
<html lang="en">
<head>
<meta charset="utf-8">
<title>Morvane – Bluetooth speakers and headsets</title>
<link rel="stylesheet" href="https://fonts.googleapis.com/css2?family=Roboto+Condensed:wght@300;400;700&display=swap">
<style>
:root{
  --orange:#f7b21b;
  --orange-deep:#f29a0f;
  --navy:#1c2a6b;
  --ink:#4a4a4a;
  --muted:#8a8a8a;
  --hero:#e6e5df;
  --panel:#f1f0eb;
  --line:#e0dccd;
  --white:#ffffff;
}
*{box-sizing:border-box;margin:0;padding:0}
html,body{width:1200px;height:800px;overflow:hidden;background:var(--white)}
body{position:relative;font-family:"Roboto Condensed",Arial,sans-serif;color:var(--ink)}
.abs{position:absolute}

/* header */
.site-header{left:0;top:0;width:1200px;height:64px;background:linear-gradient(#ffffff,#ececec)}
.brand{left:165px;top:14px;display:flex;align-items:center;gap:8px;font-size:34px;font-weight:700;color:var(--navy);letter-spacing:-.5px}
.brand .dot{width:12px;height:12px;border-radius:50%;background:var(--orange)}
.nav-item{top:12px;line-height:1}
.nav-item b{display:block;font-weight:300;font-size:21px;color:#9a9a9a}
.nav-item small{display:block;font-size:10px;font-weight:300;color:#aaa;margin-top:3px}
.nav-item.active{top:0;left:441px;width:128px;height:64px;background:var(--orange);padding:12px 0 0 20px}
.nav-item.active b,.nav-item.active small{color:#3a2a00}
.search{left:845px;top:18px;width:158px;height:30px;border:1px solid #cfcfcf;border-radius:4px;background:#fff;display:flex}
.search span{flex:1;font-size:11px;color:#b5b5b5;padding:8px 8px}
.search i{width:30px;border-left:1px solid #cfcfcf}

/* sub navigation */
.subnav{left:0;top:64px;width:1200px;height:27px;background:linear-gradient(var(--orange),var(--orange-deep))}
.subnav a{position:absolute;top:6px;font-size:11px;color:#4a3300;text-decoration:none}
.subnav a.current{top:4px;height:18px;width:136px;border-radius:9px;background:#9b8c6a;color:#fff;text-align:center;padding-top:2px}

/* hero */
.hero{left:0;top:91px;width:1200px;height:356px;background:var(--hero)}
.hero-shade{left:0;top:91px;width:1200px;height:14px;background:linear-gradient(rgba(0,0,0,.08),rgba(0,0,0,0))}
.product-shot{left:122px;top:158px;width:268px;height:240px;background:linear-gradient(#efeeea,#d9d8d2)}
.slide-arrow{width:36px;height:36px;border-radius:50%;background:#d6d5cf}
.hero-title{left:435px;top:178px;font-size:42px;font-weight:700;color:var(--orange);letter-spacing:.5px}
.hero-copy{left:437px;top:228px;width:290px;font-size:13.5px;line-height:17.5px;text-transform:uppercase;color:#555}
.hero-note{left:437px;top:316px;font-size:13.5px;color:var(--orange);text-transform:uppercase}
.btn-more{left:437px;top:349px;width:106px;height:34px;border-radius:17px;background:linear-gradient(#fafafa,#dcdcdc);border:1px solid #c9c9c9;font-size:12px;text-align:center;line-height:32px;color:#555}

/* order form */
.order-form{left:845px;top:125px;width:288px;height:530px;border-radius:18px;background:var(--panel);border:5px solid #dcdad2}
.order-tab{left:913px;top:118px;width:136px;height:60px;background:var(--orange);border-radius:0 0 18px 18px;color:#fff;font-size:15px;text-align:center;padding-top:23px;border:2px solid #fff;border-top:none}
.close{left:1101px;top:140px;width:20px;height:20px;border-radius:50%;background:var(--orange);color:#fff;font-size:12px;text-align:center;line-height:20px}
.field-label{font-size:11px;color:#666}
.field{width:208px;height:26px;border-radius:6px;background:linear-gradient(#e8e7e1,#fbfbfa);border-bottom:1px solid #fff}
.agree{left:891px;top:576px;font-size:10px;color:#777;display:flex;align-items:center;gap:7px}
.agree i{width:12px;height:12px;border-radius:50%;border:1px solid #aaa;background:#fff}
.btn-order{left:941px;top:598px;width:96px;height:26px;background:linear-gradient(90deg,#d8cfb8,#efe9d8);font-size:11px;color:#fff;padding:7px 0 0 22px}
.btn-order i{position:absolute;right:0;top:0;width:22px;height:26px;background:var(--orange)}

/* info boxes */
.info-box{top:479px;height:176px;background:#fff;border:2px solid #ece6d2;padding:16px 18px}
.info-box h2{font-size:17px;font-weight:400;color:#333;text-transform:uppercase;margin-bottom:5px}
.info-box p{font-size:9.5px;line-height:12px;color:#888}
.info-box .more{position:absolute;right:18px;bottom:10px;font-size:11px;color:var(--orange)}

/* footer */
.site-footer{left:3px;top:700px;width:1194px;height:92px;border:1px solid #ddd;background:#fff}
.footer-links{left:25px;top:734px;font-size:12.5px;color:#333;display:flex}
.footer-links span{padding:0 5px;border-left:1px solid #333}
.footer-links span:first-child{border-left:none;padding-left:0}
.social{left:25px;top:762px;display:flex;gap:13px}
.social i{width:9px;height:9px;border-radius:50%;background:#333}
.footer-about{left:620px;top:703px;width:320px;height:86px;background:linear-gradient(90deg,#f3f3f3,#fff);padding:14px 14px 0 10px;text-align:right}
.footer-about h3{font-size:10px;color:var(--orange);font-weight:700}
.footer-about p{font-size:7px;line-height:10px;color:#555}
.footer-brand{left:990px;top:730px;font-size:32px;font-weight:700;color:#7a7a7a;display:flex;align-items:center;gap:7px}
.footer-brand .dot{width:10px;height:10px;border-radius:50%;background:#9a9a9a}
</style>
</head>
<body>

<header class="abs site-header"></header>
<div class="abs brand"><span class="dot"></span>Morvane</div>
<nav>
  <div class="abs nav-item" style="left:343px"><b>HOME</b><small>Welcom to our site</small></div>
  <div class="abs nav-item active"><b>PRODUCTS</b><small>Browse our products</small></div>
  <div class="abs nav-item" style="left:592px"><b>ABOUT US</b><small>What we do</small></div>
  <div class="abs nav-item" style="left:714px"><b>CONTACT US</b><small>Keep in touch</small></div>
</nav>
<div class="abs search"><span>Search For Products</span><i></i></div>

<div class="abs subnav">
  <a style="left:195px">Product type#</a>
  <a style="left:361px">Product type#</a>
  <a style="left:529px">Product type#</a>
  <a class="current" style="left:657px">Blutooth Devices</a>
  <a style="left:872px">Headsets</a>
</div>

<section>
  <div class="abs hero"></div>
  <div class="abs hero-shade"></div>
  <div class="abs product-shot" role="img" aria-label="Product photo of the Morvane S100 compact speaker"></div>
  <div class="abs slide-arrow" style="left:52px;top:258px">
    <svg width="36" height="36"><path d="M21 12 L13 18 L21 24Z" fill="#7a7a7a"/></svg>
  </div>
  <div class="abs slide-arrow" style="left:745px;top:258px">
    <svg width="36" height="36"><path d="M15 12 L23 18 L15 24Z" fill="#7a7a7a"/></svg>
  </div>
  <h1 class="abs hero-title">MORVANE S100</h1>
  <p class="abs hero-copy">This super-small speaker delivers amazingly high quality sound! The extremely powerful bass system offers a deep and clear sound over the whole spectrum.</p>
  <p class="abs hero-note">Charging with mini USB, 3 hrs music time!</p>
  <div class="abs btn-more">READ MORE</div>
</section>

<aside>
  <div class="abs order-form"></div>
  <div class="abs order-tab">ORDER FORM</div>
  <div class="abs close">x</div>
  <div class="abs field-label" style="left:889px;top:198px">Full name:</div>
  <div class="abs field" style="left:885px;top:215px"></div>
  <div class="abs field-label" style="left:889px;top:254px">Street name:</div>
  <div class="abs field" style="left:885px;top:271px"></div>
  <div class="abs field-label" style="left:889px;top:311px">House number:</div>
  <div class="abs field" style="left:885px;top:328px"></div>
  <div class="abs field-label" style="left:892px;top:367px">Post code:</div>
  <div class="abs field" style="left:885px;top:385px"></div>
  <div class="abs field-label" style="left:891px;top:428px">City/Place:</div>
  <div class="abs field" style="left:885px;top:446px"></div>
  <div class="abs field-label" style="left:891px;top:490px">Country:</div>
  <div class="abs field" style="left:885px;top:507px"></div>
  <div class="abs agree"><i></i>I agree that the above information are correct</div>
  <div class="abs btn-order">ORDER<i></i></div>
</aside>

<section>
  <article class="abs info-box" style="left:51px;width:209px">
    <h2>About us</h2>
    <p>We specialize in design and production of top quality bluetooth equipment and we make it available to the world market at a reasonable price based on the shortest possible route from manufacturing to the consumer.</p>
    <span class="more">Read More &gt;&gt;</span>
  </article>
  <article class="abs info-box" style="left:276px;width:304px">
    <h2>Quality and insurance</h2>
    <p>Our business concept is based on optimizing design, functionality and quality assurance in making top of the line products available to our customers. Norwegians have for generations represented some of the worlds most demanding customers requiring the highest quality of the products consumed. Development and use of leading technologies are also a strong profile of Norwegians documented by the leading role in the use of information technologies and telecom as well as the leading development of oil exploration and production technologies.</p>
    <span class="more">Read More &gt;&gt;</span>
  </article>
  <article class="abs info-box" style="left:599px;width:209px">
    <h2>Products</h2>
    <p>We specialize in design and production of top quality bluetooth equipment and we make it available to the world market at a reasonable price based on the shortest possible route from manufacturing to the consumer.</p>
    <span class="more">Read More &gt;&gt;</span>
  </article>
</section>

<footer>
  <div class="abs site-footer"></div>
  <div class="abs footer-links">
    <span>Site Map</span><span>Hot News</span><span>RSS</span><span>Feeds</span><span>Media Info</span><span>Environment</span><span>Job Opportunities</span><span>Contact Us</span>
  </div>
  <div class="abs social"><i></i><i></i><i></i><i></i><i></i><i></i><i></i><i></i><i></i><i></i><i></i><i></i><i></i></div>
  <div class="abs footer-about">
    <h3>MORVANE</h3>
    <p>A simple audio portal for music lovers and their gear.</p>
    <p>Our team builds clear tools for every listener, from first-time buyers and curious visitors to loyal owners who return for new speakers and headsets.</p>
  </div>
  <div class="abs footer-brand"><span class="dot"></span>Morvane</div>
</footer>

</body>
</html>
```